Wedding on the paradise

We are getting married in Koh Samui Thailand and need booklet/ concertina that contains the invitation, event program (Day 1 Sunset Cocktail Party, Day 2 Wedding Day, Day 4 Sunset Cruise) and information about the island of Koh Samui.

Also looking for the Wedding Day Program, Menu and card containing guest names.

Below is the link to my favorite invitation and would like similar outcome.

http://www.lumeradesigns.com/wedding/couture.php?c=styles&s=destination&p=tova_marsh

We have international guests and therefore require text in Mongolian and English.

Industry/Entity Type

Wedding

Colors
cedeec

```html
<!DOCTYPE html>
<html lang="en">
<head>
<meta charset="utf-8">
<title>Koh Samui Wedding Concertina</title>
<link href="https://fonts.googleapis.com/css2?family=Great+Vibes&family=Cormorant+Garamond:wght@400;500&family=Tinos:wght@400;700&family=Open+Sans:wght@400;600&display=swap" rel="stylesheet">
<style>
:root{
  --paper:#cedeec;
  --paper-light:#e3ecf6;
  --ink:#3e8ed8;
  --ink-soft:#6aa7df;
  --navy:#12329a;
  --sea:#8fc0e8;
  --sea-deep:#5ea6de;
  --page:#ffffff;
}
*{margin:0;padding:0;box-sizing:border-box}
html,body{width:900px;height:1200px;overflow:hidden;background:var(--page)}
.canvas{position:relative;width:900px;height:1200px}
.panel{position:absolute;background:radial-gradient(ellipse at 40% 35%,var(--paper-light),var(--paper) 80%);color:var(--ink);font-family:'Tinos',serif;overflow:hidden}
.art{position:absolute;border-radius:4px}
.map{background:linear-gradient(115deg,var(--paper-light) 0%,var(--sea) 45%,var(--sea-deep) 75%,var(--sea) 100%)}
.figure{background:radial-gradient(ellipse,var(--sea) 0%,transparent 70%)}
.script{font-family:'Great Vibes',cursive;color:var(--navy);font-weight:400;line-height:1}
.sub{font-family:'Open Sans',sans-serif;color:var(--navy);font-size:9px;letter-spacing:.5px}
.center{text-align:center}
.body{font-size:7px;line-height:1.45}
.rule{position:absolute;height:1px;background:var(--ink-soft)}

/* cover */
.cover{left:38px;top:33px;width:226px;height:320px}
.cover-title{position:absolute;top:176px;width:100%;font-family:'Cormorant Garamond',serif;font-size:21px;letter-spacing:1px;color:var(--ink-soft)}
.cover-date{position:absolute;top:206px;width:100%;font-size:7px}

/* invitation spread */
.spread{left:320px;top:15px;width:505px;height:355px}
.invite{position:absolute;left:252px;top:0;width:253px;height:355px}

/* info row */
.map-panel{left:18px;top:428px;width:217px;height:352px}
.info{left:323px;top:428px;width:255px;height:352px}
.info-block{position:absolute;left:20px;width:220px}
.info-block h4{font-weight:400;font-size:7px;margin-bottom:5px}
.info-block p{font-size:5.5px;line-height:1.5;padding-left:12px;margin-bottom:3px}
.travel{left:622px;top:428px;width:250px;height:352px}
.travel-lead{position:absolute;left:15px;top:92px;font-size:7.5px;font-weight:700}
.pack-title{position:absolute;left:146px;top:126px;font-size:7.5px;font-weight:700}
.pack-list{position:absolute;left:130px;top:152px;list-style:none}
.pack-list li{font-size:6.5px;font-weight:700;margin-bottom:13.5px;padding-left:10px;position:relative}
.pack-list li::before{content:"";position:absolute;left:0;top:1px;width:4px;height:4px;border:1px solid var(--ink);transform:rotate(45deg)}

/* concertina */
.program{left:5px;top:825px;width:885px;height:310px}
.fold{position:absolute;top:0;width:1px;height:310px;border-left:1px dashed rgba(62,142,216,.25)}
.welcome-title{position:absolute;left:0;width:221px;top:80px;font-family:'Tinos',serif;font-size:16px;color:var(--ink)}
.welcome-sub{position:absolute;left:0;width:221px;top:98px}
.welcome-text{position:absolute;left:14px;width:200px;top:118px;font-size:7px;line-height:1.4;text-align:center}
.sign{position:absolute;left:0;width:221px;top:258px}
</style>
</head>
<body>
<div class="canvas">

  <!-- Cover -->
  <section class="panel cover">
    <div class="art figure" role="img" aria-label="Line drawing of an elephant" style="left:84px;top:100px;width:60px;height:70px"></div>
    <h1 class="cover-title center">KOH SAMUI</h1>
    <p class="cover-date center">December 2014</p>
  </section>

  <!-- Invitation spread -->
  <section class="panel spread">
    <div class="art map" role="img" aria-label="Map of the Koh Samui coastline" style="left:0;top:0;width:252px;height:355px;border-radius:0"></div>
    <div class="invite">
      <h2 class="script center" style="position:absolute;top:32px;width:100%;font-size:24px">Invitation</h2>
      <p class="sub center" style="position:absolute;top:57px;width:100%">УРИЛГА</p>
      <div class="art figure" role="img" aria-label="Line drawing of a Thai dancer figure" style="left:100px;top:75px;width:52px;height:95px"></div>
      <div class="rule" style="left:96px;top:172px;width:60px"></div>
      <div class="body center" style="position:absolute;top:170px;left:10px;width:233px">
        <p>Together with their parents Selene &amp; Marek would like to invite</p>
        <p>ХАМТЫН АМЬДРАЛАА ТЭМДЭГЛЭХ ЁСЛОЛ</p>
        <p style="margin-top:14px;text-align:left;padding-left:36px">Эрхэм хүндэт ..........................................................</p>
        <p style="margin-top:10px">to celebrate their union.</p>
        <p>Saturday, December 13, 2014</p>
        <p>Ceremony at four o'clock in the afternoon</p>
        <p>Baan Sairung Lipa Noi Koh Samui</p>
        <p style="margin-top:10px">таныг гэр бүлийн хамт</p>
        <p>Бидний хамтын амьдралын эхлэлийг тэмдэглэх ёслолд</p>
        <p>хүрэлцэн ирэхийг урьж байна.</p>
        <p>Огноо: 2014 оны 12 сарын 13, Бямба гараг</p>
        <p>Байршил: Баан Сайрунг Липа Ной, Кох Самуи, Тайланд</p>
      </div>
    </div>
  </section>

  <!-- Map panel -->
  <section class="panel map-panel">
    <div class="art map" role="img" aria-label="Map of the Koh Samui coastline with beaches" style="left:0;top:0;width:217px;height:352px;border-radius:0"></div>
  </section>

  <!-- Info -->
  <section class="panel info">
    <div class="art figure" role="img" aria-label="Line drawing of an elephant" style="left:85px;top:6px;width:62px;height:44px"></div>
    <h2 class="script center" style="position:absolute;top:58px;width:100%;font-size:19px">Info</h2>
    <p class="sub center" style="position:absolute;top:78px;width:100%;font-size:7px">МЭДЭЭЛЭЛ</p>
    <div class="info-block" style="top:93px">
      <h4>Dress / Хувцаслалт</h4>
      <p>Smart Casual<br>'Ухаалаг' энгийн</p>
    </div>
    <div class="info-block" style="top:128px">
      <h4>Getting there / Очих</h4>
      <p>There will be a shuttle bus from Bo Phut to the ceremony. Please let us know if you are interested.</p>
      <p>Бо Пхутаас ёслолын газар хүртэл автобус явна. Хэрэгтэй бол бидэнд мэдэгдээрэй.</p>
    </div>
    <div class="info-block" style="top:180px">
      <h4>Gifts / Бэлэг</h4>
      <p>Your presence at our wedding is the greatest gift of all.</p>
      <p>Та бүхэн ирж баярыг хуваалцах нь бидэнд хамгийн том бэлэг юм.</p>
    </div>
    <div class="info-block" style="top:218px">
      <h4>Champagne/Wine / Шампань/Дарс</h4>
      <p>Koh Samui is a tropical island where champagne and wine can be dear. For your enjoyment we advise our guests to bring a bottle of champagne or red wine with you.</p>
      <p>Кох Самуи арал дээр шампань, дарс үнэтэй байдаг тул нэг лонх авчрахыг зөвлөж байна. Ингэснээр та илүү таатай амрах болно.</p>
    </div>
    <div class="info-block" style="top:282px">
      <h4>Our website / Манай вэб хуудас</h4>
      <p>Please check for any updates or changes in our wedding site selene-marekweds.com</p>
      <p>Шинэ мэдээллийг манай хуудаснаас харна уу (selene-marekweds.com)</p>
    </div>
    <div class="rule" style="left:96px;top:340px;width:62px"></div>
  </section>

  <!-- Travel info -->
  <section class="panel travel">
    <h2 class="script center" style="position:absolute;top:28px;width:100%;font-size:19px">Travel Info</h2>
    <p class="sub center" style="position:absolute;top:48px;width:100%;font-size:7px">МЭДЭЭЛЭЛ</p>
    <p class="travel-lead">Read and watch on Thailand before travel</p>
    <div class="art" style="left:14px;top:122px;width:108px;height:160px;background:var(--sea)"></div>
    <div class="art" role="img" aria-label="Cover of a travel film set on a Thai beach" style="left:19px;top:128px;width:98px;height:68px;background:linear-gradient(160deg,#4d8fb8,#c9a36a)"></div>
    <div class="art" role="img" aria-label="Cover of a Thailand travel guide" style="left:70px;top:166px;width:46px;height:50px;background:linear-gradient(#f4f0e6,#d9c27a)"></div>
    <div class="art" role="img" aria-label="Cover of a comedy film set in Bangkok" style="left:19px;top:218px;width:98px;height:60px;background:linear-gradient(160deg,#6b7f5a,#b98d64)"></div>
    <p class="pack-title">What to pack for Thailand</p>
    <ul class="pack-list">
      <li>Consider your hosts</li>
      <li>Remember the climate</li>
      <li>Consider activities</li>
      <li>Be aware of sun</li>
      <li>Champagne</li>
      <li>Insect repellent</li>
      <li>Travel adapter</li>
    </ul>
  </section>

  <!-- Program concertina -->
  <section class="panel program">
    <div class="fold" style="left:221px"></div>
    <div class="fold" style="left:442px"></div>
    <div class="fold" style="left:663px"></div>

    <!-- Welcome -->
    <div class="art figure" role="img" aria-label="Monogram wreath ornament" style="left:80px;top:8px;width:62px;height:62px;border-radius:50%"></div>
    <h2 class="welcome-title center">WELCOME</h2>
    <p class="welcome-sub center" style="font-size:9.5px;color:var(--ink)">ТАВТАЙ МОРИЛНО УУ</p>
    <div class="welcome-text">
      <p>To our family and friends, it means the world to us to have you here. Thank you for the support, love and laughter you have contributed to our lives. We hope you enjoy and relax your time in Koh Samui. Here is the weekend full of LOVE.</p>
      <p style="margin-top:8px">Гэр бүлийнхэн болон дотны анд нөхөддөө хандаж, бидэнтэй хамт байгаад баярлаж байна. Та бүхний дэмжлэг, хайр, инээд хөөр бидний амьдралыг баяжуулсан билээ. Кох Самуид тухтай амарч, хайраар дүүрэн амралтын өдрүүдийг өнгөрүүлээрэй.</p>
    </div>
    <div class="sign center">
      <p class="script" style="font-size:23px">Selene &amp; Marek</p>
      <p class="sub" style="margin-top:2px">Селене &amp; Марек</p>
    </div>

    <!-- Sunset cocktail -->
    <div class="art figure" role="img" aria-label="Line drawing of a lone tree" style="left:292px;top:10px;width:80px;height:60px"></div>
    <h3 class="script center" style="position:absolute;left:221px;width:221px;top:84px;font-size:23px">Sunset Cocktail</h3>
    <p class="sub center" style="position:absolute;left:221px;width:221px;top:110px">Наран Жаргах Коктейл</p>
    <div class="body center" style="position:absolute;left:236px;width:191px;top:142px;font-size:7.5px">
      <p>At the first day with us, we relax, sip cocktail by the pool and enjoy beautiful Koh Samui.</p>
      <p style="margin-top:10px">Бид бүгд хамтдаа байх эхний өдөр усан сангийн дэргэд коктейль шимэн Кох Самуигийн үзэсгэлэнт байгальд амарна.</p>
      <p style="margin-top:12px">Baan Sairung 3pm<br>Баан Сайрунг 15:00 цаг</p>
    </div>

    <!-- Wedding day -->
    <div class="art figure" role="img" aria-label="Row of Thai dancers in traditional costume" style="left:460px;top:5px;width:190px;height:135px;border-radius:6px"></div>
    <div class="rule" style="left:452px;top:140px;width:200px"></div>
    <h3 class="script center" style="position:absolute;left:442px;width:221px;top:150px;font-size:23px">Wedding Day</h3>
    <p class="sub center" style="position:absolute;left:442px;width:221px;top:175px">Хуримын өдөр</p>
    <div class="body center" style="position:absolute;left:452px;width:201px;top:200px;font-size:7.5px">
      <p>Ceremony at 5 pm followed by celebration<br>Transportation from Bo Phut departing from 3.45 pm</p>
      <p style="margin-top:10px">Ёслолын арга хэмжээ 17:00 цагт эхэлнэ<br>Бо Пхутаас унаа 15:45-д явна</p>
    </div>
    <div class="rule" style="left:452px;top:273px;width:200px"></div>

    <!-- Sunset cruise -->
    <h3 class="script" style="position:absolute;left:758px;top:22px;font-size:23px">Sunset Cruise</h3>
    <p class="sub" style="position:absolute;left:766px;top:48px">Наран Жаргах Круиз</p>
    <div class="body center" style="position:absolute;left:740px;width:140px;top:68px;font-size:7.5px">
      <p>Post Wedding Chillax<br>Хуримын дараах өдрийн аялал</p>
    </div>
    <div class="art figure" role="img" aria-label="Sketch of a sailboat on the sea" style="left:695px;top:110px;width:180px;height:195px;border-radius:8px"></div>
  </section>

</div>
</body>
</html>
```